Podcast cover art for Steady Harbor Podcast for Busy Parents

I am relaunching my 3 year podcast under a new name. The podcast is called Steady Harbor for Busy Parents. The parent company is called Bright Path Studio (see attached logo) and should be represented on the cover in a small way. Previously the show was called Bright Path Studio. We talk about creating life balance for working moms by focusing on faith, marriage, parenting, career, health, home, finances, and friends/fun. I don't mind having stock photography on the cover but I prefer not to have my image on it as it is not a personal brand. I have attached a couple of stock images as inspiration.

Target Market(s)

working Christian moms age 30-45 income 75,000+, working full time, Christian faith, married

Industry/Entity Type

Media

Font styles to use
Serif

Requirements
Must have
• Podcast name: Steady Harbor for Busy Parents
• By: Bright Path Studio (include logo)
• I also included my brand sheet for reference which includes my brand colors and fonts. Navy should be the primary with orange and gray as the accents
Should not have
• No flowers, or overly girly. My brand is more clean, preppy, and young-sophisticated.

```html
<!DOCTYPE html>
<html lang="en">
<head>
<meta charset="utf-8">
<title>Steady Harbor for Busy Parents — Podcast Cover</title>
<link rel="stylesheet" href="https://fonts.googleapis.com/css2?family=Montserrat:wght@300;400;700&display=swap">
<style>
  :root {
    --navy: #2b2f3b;
    --orange: #f26522;
    --white: #ffffff;
    --page: #eef0f3;
  }
  * { box-sizing: border-box; margin: 0; padding: 0; }
  html, body {
    width: 1200px;
    height: 870px;
    overflow: hidden;
    background: var(--page);
  }
  .canvas {
    position: relative;
    width: 1200px;
    height: 870px;
    display: flex;
    align-items: center;
    justify-content: center;
  }
  .cover {
    position: relative;
    width: 700px;
    height: 700px;
    background: var(--navy);
    font-family: "Montserrat", sans-serif;
    color: var(--white);
    text-align: center;
  }
  .topic-pill {
    position: absolute;
    left: 58px;
    width: 584px;
    height: 40px;
    border-radius: 20px;
    background: var(--white);
    display: flex;
    align-items: center;
    justify-content: center;
    gap: 14px;
    font-weight: 700;
    font-size: 21px;
    letter-spacing: 0.04em;
    color: var(--orange);
  }
  .topic-pill--top { top: 81px; }
  .topic-pill--bottom { top: 426px; }
  .topic-pill .dot {
    width: 9px;
    height: 9px;
    border-radius: 50%;
    background: var(--navy);
  }
  .show-title {
    position: absolute;
    left: 0;
    right: 0;
    top: 158px;
    font-weight: 300;
    text-shadow: 0 3px 6px rgba(0,0,0,0.35);
  }
  .show-title__main {
    display: block;
    font-size: 88px;
    line-height: 86px;
    letter-spacing: 0.01em;
  }
  .show-title__sub {
    display: block;
    margin-top: 10px;
    font-size: 46px;
    line-height: 50px;
    letter-spacing: 0.03em;
  }
  .studio-name {
    position: absolute;
    left: 0;
    right: 0;
    top: 590px;
    font-weight: 400;
    font-size: 46px;
    color: var(--orange);
  }
</style>
</head>
<body>
  <main class="canvas">
    <section class="cover" aria-label="Steady Harbor for Busy Parents podcast cover">
      <div class="topic-pill topic-pill--top">
        <span>FAITH</span><span class="dot"></span>
        <span>MARRIAGE</span><span class="dot"></span>
        <span>PARENTING</span><span class="dot"></span>
        <span>CAREER</span>
      </div>
      <h1 class="show-title">
        <span class="show-title__main">STEADY<br>HARBOR</span>
        <span class="show-title__sub">FOR BUSY PARENTS</span>
      </h1>
      <div class="topic-pill topic-pill--bottom">
        <span>HEALTH</span><span class="dot"></span>
        <span>HOME</span><span class="dot"></span>
        <span>FINANCES</span><span class="dot"></span>
        <span>FRIENDSHIP</span>
      </div>
      <p class="studio-name">Bright Path Studio</p>
    </section>
  </main>
</body>
</html>
```